Box Truck Design for a Custom Bedding company in the Marine Industry

We are looking for a creative Modern design for our box truck. I needs to Include our Icon (sailboat, moon and water) and perhaps our full logo with our stylized name of harborslumber.net. It needs to include out phone number" (800) 555-2741 our website written out "www.harborslumber.net" and our service offering of " Custom Boat Mattresses and Bedding" . Our box will be silver. I've included a pdf of the general shape of our box as it's a former Q-move truck so it has a part of the box that over hangs the cab. We want a design that is modern an clean but still catches the eye. In the pdf of the mock up there is a dark silver strip. That is metal trim that will not be wrapped. And the strip of grey below the metal trim has texture so information can not be placed there, however feel free to change the color of that section or or place part of the overall design in that section. I don't need design for the front of the truck or the back. I just need the side artwork, unless you have an idea for the back that looks great with the sides.

Font styles to use
Serif
Sans Serif

Colors
0655a3
ec1f27
ffffff

Requirements
Must have
• The mock up should show the background of the box as silver and the cab of the truck as silver as well.
Nice to have
• We like the look of having our Icon (Sailboat, Moon and Water) really large on the Box and towards the back of the truck.
Should not have
• We do not want to have pictures of beds or our products on the truck.

```html
<!DOCTYPE html>
<html lang="en">
<head>
<meta charset="utf-8">
<title>Harbor Slumber – Box Truck Side Wrap</title>
<link rel="stylesheet" href="https://fonts.googleapis.com/css2?family=Rubik:wght@700;800&family=Roboto:wght@400;500&display=swap">
<style>
  :root {
    --page: #eef1f4;
    --box-silver: #e9ebee;
    --box-edge: #c9ced4;
    --wrap-red: #cc0000;
    --deep-navy: #0b1a54;
    --gap-silver: #c7d3e2;
    --text-white: #ffffff;
  }
  html, body {
    margin: 0;
    width: 1200px;
    height: 900px;
    overflow: hidden;
    background: var(--page);
  }
  .canvas {
    position: relative;
    width: 1200px;
    height: 900px;
  }
  .truck-side {
    position: absolute;
    inset: 0;
  }
  .tagline {
    font-family: "Rubik", "Arial Black", sans-serif;
    font-weight: 800;
    font-size: 32px;
    fill: var(--text-white);
    letter-spacing: 0.3px;
  }
  .phone {
    font-family: "Roboto", Arial, sans-serif;
    font-weight: 500;
    font-size: 33px;
    fill: var(--text-white);
  }
  .web {
    font-family: "Roboto", Arial, sans-serif;
    font-weight: 400;
    font-size: 25px;
    fill: var(--text-white);
  }
  .brand-name {
    font-family: "Rubik", "Arial Black", sans-serif;
    font-weight: 800;
    font-size: 44px;
    fill: var(--text-white);
  }
</style>
</head>
<body>
<div class="canvas">
  <svg class="truck-side" width="1200" height="900" viewBox="0 0 1200 900" xmlns="http://www.w3.org/2000/svg">
    <!-- box panel -->
    <rect class="box-panel" x="60" y="200" width="1080" height="493" rx="6" fill="var(--box-silver)" stroke="var(--box-edge)" stroke-width="3"/>

    <!-- stepped red wrap panel (upper reaches over the cab) -->
    <path class="wrap-panel" d="M470 236 H1084 Q1102 236 1102 254 V385 H888 V654 H470 Z" fill="var(--wrap-red)"/>

    <!-- brand mark area: plain circle with name -->
    <circle class="brand-ring" cx="414" cy="431" r="206" fill="var(--gap-silver)"/>
    <circle class="brand-disc" cx="414" cy="431" r="196" fill="var(--deep-navy)"/>
    <text class="brand-name" x="414" y="420" text-anchor="middle">Harbor</text>
    <text class="brand-name" x="414" y="472" text-anchor="middle">Slumber</text>

    <!-- service offering -->
    <text class="tagline" x="845" y="302" text-anchor="middle">Custom Boat Mattresses</text>
    <text class="tagline" x="845" y="342" text-anchor="middle">and Bedding</text>

    <!-- contact -->
    <text class="phone" x="858" y="590" text-anchor="end">(800) 555-2741</text>
    <text class="web" x="858" y="625" text-anchor="end">www.harborslumber.net</text>
  </svg>
</div>
</body>
</html>
```